Webdesign für Entwickler von onlinebasierten Terminformularen
Super Designs. Schnell und motiviert. Danke für die hervorragende Umsetzung und die Ideen!
Zielgruppe
Deutsch:
Wir sind ein Startup, das über die Seite Kalendrio.de zukünftig folgenden Service anbietet: Unternehmer können sehr flexibel (selbst) gestaltete Terminformulare erstellen und auf Ihrer Website einbinden. Kunden können dann diese Termine buchen und bekommen dann Erinnerungs-Mails und SMS.
Zielgruppe: Dienstleister wie Fotografen, Friseure, Versicherungsvertreter, Masseure, Restaurants, Arztpraxen. Also alle, die darauf angewiesen sind, dass vereinbarte Termine eingehalten werden und die die Terminvereinbarung vereinfachen wollen. Also weniger per Telefon, mehr über die eigene Website.
Englisch:
We are a start up, that is going to offer this services on the Website Kalendrio.de :
Companies can create highly flexible (self-designed) appointment forms and integrate them on their website. Customer can book appointments and will get an reminding email and SMS.
Target group: Service providers such as photographers, hairdressers, insurance agents, masseurs, restaurants, medical offices. So all those who depend on meeting agreed appointments and who want to simplify the appointment. Less by telephone, more over their own website.
Aufgabenstellung
Übersichtlichkeit, genug Weißraum, deutliche, große Überschriften, Seriös aber gerne frische Farben bei einzelnen Elementen (z.B. bei Icons oder bei Handlungsaufforderungs-Buttons), Trennlinien, Inhalte auf den Punkt.
Logo-Entwurf anbei (wird gerade hier über entwurfhafen.de ebenfalls erstellt/optimiert, siehe #817306) sagt das wesentliche aus.
Kalendrio soll also ein sehr nützliches Tool sein, das jeder schnell versteht. Daher muss auch die Website sehr übersichtlich und klar aufgebaut werden. Die wesentlichen Aussagen/Menüpunkte finden sich auf der Startseite (bzw. im Hauptmenü, siehe grober Entwurf anbei).
- frische Farben (z.B. grün, orange, gelb)
- seröse Farben/Grauwerte (z.B. blau, grau, schwarz)
- Hauptmenü/Metanavigation/Footer-Bereich
Das Design und das Teaser-Bild (Frau mit Hammer) auf dem Entwurf anbei (seite1_mit_teaser_entwurf2.jpg) sind nur als grobe Ideen (Richtung) zu verstehen. Die Startseite muss also keine Teaser-Bilder enthalten.
Der Entwurf anbei soll lediglich die ungefähre Richtung mit den angedachten Menüpunkten verdeutlichen.
Übersichtlich und modern finden wir z.B. https://talkroomly.example/de (viel Weißraum, farbige Icons, Infos übersichtlich dargeboten, lächelnde Gesichter) und übrigens auch https://www.entwurfhafen.example.
Bitte entwerfen Sie (erstmal) drei Seiten:
- Startseite
- Funktionen/Preis (Beispiel auf https://talkroomly.example/de/tools Und/oder in Tabellenform wie auf https://talkroomly.example/de/pricing/ siehe Content-Plan anbei)
- Über Kalendrio (Über uns, siehe Content-Plan anbei)
Der Content-Plan soll das Projekt verdeutlichen.
Anmerkung von unserem Programmierer: Praktisch wäre eine Basis auf Bootstrap. Dies ist aber keine Pflicht! Das Design/die Idee geht vor :-)
1zu1-Folgeaufträge (für dieses und andere Projekte im Bereich Webdesign, Flyer, CorporateDesign, Grafiken) sind sehr wahrsc..

```html
<!DOCTYPE html>
<html lang="de">
<head>
<meta charset="utf-8">
<title>Kalendrio – Funktionen &amp; Preise</title>
<link href="https://fonts.googleapis.com/css2?family=Catamaran:wght@300;400;500;600;700&display=swap" rel="stylesheet">
<style>
:root{
  --slate:#6f7b81;
  --slate-dark:#5a646a;
  --charcoal:#454545;
  --green:#8cbf45;
  --text:#5d666b;
  --muted:#9aa1a5;
  --card-bg:#f7f7f7;
  --line:#dcdfe0;
  --white:#fff;
}
*{box-sizing:border-box;margin:0;padding:0}
html,body{width:1200px;height:2657px;overflow:hidden}
body{font-family:"Catamaran",sans-serif;color:var(--text);background:var(--white);position:relative}
.abs{position:absolute}
.center{text-align:center;left:0;width:1200px}
.btn{display:flex;align-items:center;justify-content:center;background:var(--green);color:var(--white);font-weight:600;font-size:14px}

.meta-bar{top:0;left:0;width:1200px;height:32px;background:var(--slate);color:var(--white);font-size:9px;font-weight:500}
.meta-bar span{position:absolute;top:10px}
.meta-bar .sep{width:1px;height:11px;background:rgba(255,255,255,.5);top:11px}

.main-nav{top:32px;left:0;width:1200px;height:52px;background:var(--white);font-size:11px;border-bottom:1px solid #eee}
.brand{position:absolute;left:238px;top:12px;display:flex;align-items:center;gap:6px;font-size:24px;font-weight:600;color:var(--slate)}
.brand i{width:14px;height:14px;background:var(--slate);display:block}
.main-nav a{position:absolute;top:19px;color:var(--text);text-decoration:none}
.main-nav a.active{color:var(--slate-dark)}
.main-nav a.active::after{content:"";position:absolute;left:0;right:0;top:20px;height:2px;background:var(--green)}
.nav-signup{position:absolute;left:890px;top:11px;width:93px;height:29px;border:1.5px solid var(--green);border-radius:15px;font-size:11px;display:flex;align-items:center;justify-content:center}

.hero{top:84px;left:0;width:1200px;height:285px;background:var(--slate);color:var(--white)}
.hero h1{position:absolute;top:74px;font-size:27px;font-weight:600}
.hero p{position:absolute;top:114px;font-size:17px;font-weight:300}

.plan{width:244px;background:var(--card-bg);box-shadow:0 2px 6px rgba(0,0,0,.06);top:290px}
.plan-head{height:115px;background:var(--charcoal);color:var(--white);text-align:center;padding-top:24px}
.plan-head h2{font-size:18px;font-weight:600}
.tag{display:inline-block;margin-top:4px;padding:1px 12px;font-size:11px;font-weight:700;background:#8d8d8d;color:var(--white)}
.tag.light{background:var(--white);color:var(--green)}
.tag.ext{background:var(--green)}
.price{position:absolute;top:90px;left:28px;width:188px;height:50px;background:var(--white);text-align:center;font-size:16px;line-height:52px}
.plan .btn{position:absolute;top:140px;left:28px;width:188px;height:37px;font-size:12px}
.features{list-style:none;text-align:center;font-size:9.5px;padding-top:90px}
.features li{line-height:12px;margin-bottom:17px}
.more{position:absolute;left:0;bottom:0;width:244px;height:56px;background:var(--white);box-shadow:0 4px 8px rgba(0,0,0,.08);text-align:center;line-height:56px;font-size:12px;font-weight:600}

.divider{top:914px;left:213px;width:776px;height:1px;background:var(--line)}

.section-title{font-size:26px;font-weight:600;color:var(--slate)}
.section-sub{font-size:15px}
.step{width:262px;text-align:center}
.step svg{display:block;margin:0 auto}
.step h3{font-size:13px;font-weight:500;line-height:17px;margin-top:20px;height:44px}
.step hr{width:31px;border:0;height:2px;background:var(--green);margin:0 auto 18px}
.step p{font-size:9px;color:var(--muted);line-height:12px}
.arrow{top:1128px}

.banner{top:1491px;left:0;width:1200px;height:406px;background:linear-gradient(120deg,#3d4347 0%,#6a5e57 35%,#7a7f82 60%,#3e4245 100%)}
.banner-content{top:1612px;color:var(--white)}
.banner-content h2{font-size:27px;font-weight:600}
.banner-content p{font-size:17px;font-weight:300;line-height:24px;margin-top:8px}

.svc{top:2103px;width:375px;height:244px;background:#f3f3f3;overflow:hidden}
.svc h3{position:absolute;left:38px;top:48px;font-size:19px;font-weight:600;color:var(--slate);line-height:24px}
.svc hr{position:absolute;left:38px;top:112px;width:50px;border:0;height:2px;background:var(--green)}
.svc p{position:absolute;left:38px;top:124px;font-size:9.5px;line-height:14px}
.svc .link{position:absolute;left:38px;top:164px;height:42px;padding:0 20px;background:var(--slate);color:var(--white);font-size:12px;font-weight:600;display:flex;align-items:center;gap:10px}
.svc .link b{color:var(--green);font-weight:400}
.svc .art{position:absolute;right:0;top:0;width:190px;height:244px;background:linear-gradient(135deg,#f3f3f3,#e4e6e7)}

.footer-top{top:2445px;left:0;width:1200px;height:68px;background:var(--slate)}
.footer-top .brand{left:214px;top:20px;color:var(--white)}
.footer-top .brand i{background:var(--white)}
.footer{top:2513px;left:0;width:1200px;height:144px;background:var(--slate-dark);color:var(--white);font-size:9.5px}
.footer .col{position:absolute;top:18px;line-height:17.5px}
.footer .col strong{display:block;font-weight:500;margin-bottom:6px}
.footer .col span{display:block;opacity:.85}
.lang{position:absolute;left:214px;top:54px;width:144px;height:30px;border:1px solid rgba(255,255,255,.7);border-radius:15px;display:flex;align-items:center;padding-left:20px;gap:14px}
.footer .btn{position:absolute;left:801px;top:104px;width:181px;height:38px;font-size:11px}
</style>
</head>
<body>

<div class="abs meta-bar">
  <span style="left:799px">Kontakt</span><i class="abs sep" style="left:837px"></i>
  <span style="left:847px">DE ⌄</span><i class="abs sep" style="left:878px"></i>
  <span style="left:889px">Zu Wertwelle wechseln</span>
</div>

<nav class="abs main-nav">
  <div class="brand"><i></i>Kalendrio</div>
  <a class="active" style="left:377px">Funktionen / Preis</a>
  <a style="left:496px">Help-Center</a>
  <a style="left:590px">Über Uns</a>
  <a style="left:669px">Blog</a>
  <a style="left:852px">Login</a>
  <div class="nav-signup">Konto erstellen</div>
</nav>

<header class="abs hero">
  <h1 class="abs center">Funktionen &amp; Preise</h1>
  <p class="abs center">Hier finden Sie alle Informationen und Hilfen rund um Kalendrio.</p>
</header>

<section class="abs plan" style="left:212px;height:404px">
  <div class="plan-head"><h2>Kalendrio</h2><span class="tag">Free</span></div>
  <div class="price">Kostenlos</div>
  <div class="btn">Jetzt anmelden</div>
  <ul class="features" style="padding-top:95px">
    <li>Umfragen mit Teaser-Foto<br>oder Clipstrom-Video</li>
    <li>Formular-Generator</li>
    <li>Termin-Assistent (Wizzard)</li>
    <li>Branchenspezifische Vorlagen</li>
  </ul>
  <div class="more">Mehr erfahren</div>
</section>

<section class="abs plan" style="left:475px;height:490px">
  <div class="plan-head"><h2>Kalendrio</h2><span class="tag light">Light</span></div>
  <div class="price">14,99 € pro Monat</div>
  <div class="btn">Jetzt anmelden</div>
  <ul class="features">
    <li>Umfragen mit Teaser-Foto<br>oder Clipstrom-Video</li>
    <li>Formular-Generator</li>
    <li>Termin-Assistent (Wizzard)</li>
    <li>Branchenspezifische Vorlagen</li>
    <li>Termin mit Bewertungs-Tool<br>Wertwelle verknüpfen</li>
    <li>Teilnehmerliste als CSV / PDF-Export</li>
    <li>Serientermine</li>
  </ul>
  <div class="more">Mehr erfahren</div>
</section>

<section class="abs plan" style="left:737px;height:549px">
  <div class="plan-head"><h2>Kalendrio</h2><span class="tag ext">Extended</span></div>
  <div class="price">29,99 € pro Monat</div>
  <div class="btn">Jetzt anmelden</div>
  <ul class="features">
    <li>Umfragen mit Teaser-Foto<br>oder Clipstrom-Video</li>
    <li>Formular-Generator</li>
    <li>Termin-Assistent (Wizzard)</li>
    <li>Branchenspezifische Vorlagen</li>
    <li>Termin mit Bewertungs-Tool<br>Wertwelle verknüpfen</li>
    <li>Teilnehmerliste als CSV / PDF-Export</li>
    <li>Serientermine</li>
    <li>Termin duplizieren</li>
    <li>Statora-Analytics Einbindung uvm...</li>
  </ul>
  <div class="more">Mehr erfahren</div>
</section>

<div class="abs divider"></div>

<h2 class="abs center section-title" style="top:985px">Und so funktioniert's</h2>
<p class="abs center section-sub" style="top:1021px">In nur 3 Schritten zum ganz individuellen Terminformular</p>

<div class="abs step" style="left:205px;top:1117px">
  <svg width="40" height="40" viewBox="0 0 40 40" fill="none" stroke="#8cbf45" stroke-width="2"><circle cx="17" cy="10" r="7"/><path d="M3 37v-5c0-6 6-10 14-10 3 0 5 .5 7 1.5"/><path d="M26 36l10-10 2 2-10 10h-2z"/></svg>
  <h3>Kostenlose Anmeldung bei Kalendrio.de</h3><hr>
  <p>Melden Sie sich kostenlos bei Kalendrio an<br>und organisieren Sie noch heute<br>Ihre Kundentermine.</p>
</div>
<svg class="abs arrow" style="left:466px" width="12" height="20" viewBox="0 0 12 20" fill="none" stroke="#7a8287" stroke-width="1.5"><path d="M2 2l8 8-8 8"/></svg>
<div class="abs step" style="left:467px;top:1117px">
  <svg width="40" height="40" viewBox="0 0 40 40" fill="none" stroke="#8cbf45" stroke-width="2"><rect x="6" y="3" width="26" height="32"/><path d="M3 7v31h24"/><path d="M12 12h14M12 18h14M12 24h8"/><circle cx="30" cy="31" r="6" fill="#8cbf45"/><path d="M27 31l2 2 4-4" stroke="#fff"/></svg>
  <h3>Formular erstellen &amp;<br>einbinden</h3><hr>
  <p>Melden Sie sich kostenlos bei Kalendrio an<br>und organisieren Sie noch heute<br>Ihre Kundentermine.</p>
</div>
<svg class="abs arrow" style="left:728px" width="12" height="20" viewBox="0 0 12 20" fill="none" stroke="#7a8287" stroke-width="1.5"><path d="M2 2l8 8-8 8"/></svg>
<div class="abs step" style="left:729px;top:1117px">
  <svg width="40" height="40" viewBox="0 0 40 40" fill="none" stroke="#8cbf45" stroke-width="2"><path d="M8 14a15 15 0 1 1 6 20"/><path d="M22 10v11h8"/><path d="M8 35l-5-5a3 3 0 0 1 5-4 3 3 0 0 1 5 4z" fill="#8cbf45"/></svg>
  <h3>Termine verwalten.<br>Schnell, einfach &amp; flexibel.</h3><hr>
  <p>Melden Sie sich kostenlos bei Kalendrio an<br>und organisieren Sie noch heute<br>Ihre Kundentermine.</p>
</div>

<div class="abs btn" style="left:423px;top:1348px;width:354px;height:50px">Jetzt kostenlos Konto erstellen</div>

<div class="abs banner" role="img" aria-label="Unscharfes Foto eines Arbeitsplatzes mit Kaffeetasse und Laptop"></div>
<div class="abs center banner-content">
  <h2>Holen Sie sich jetzt Kalendrio</h2>
  <p>Profitieren Sie jetzt von Kalendrio und sichern Sie sich<br>alle Vorteile. Verwalten Sie jetzt Ihre Termine.</p>
</div>
<div class="abs btn" style="left:423px;top:1722px;width:354px;height:50px">Jetzt kostenlos Konto erstellen</div>

<h2 class="abs center section-title" style="top:1966px">Kalendrio - Service</h2>
<p class="abs center" style="top:2010px;font-size:12.5px;line-height:24px;color:var(--muted)">Dann nutzen Sie gerne unsere Service-Angebote. In unserem Help-Center finden Sie sicher eine Lösung<br>für Ihre Probleme und im Blog finden Sie die aktuellsten Neuigkeiten rund um Kalendrio.</p>

<div class="abs svc" style="left:215px">
  <div class="art" role="img" aria-label="Illustration schwebender Karten mit Fragezeichen"></div>
  <h3>Kalendrio<br>Help-Center</h3>
  <p style="top:120px">Sie haben Fragen? Dann nutzen Sie<br>gerne unser Help-Center.</p>
  <div class="link"><b>›</b>Weiter zum Help-Center</div>
</div>
<div class="abs svc" style="left:608px">
  <div class="art" role="img" aria-label="Illustration gestapelter Blogartikel-Karten"></div>
  <h3>Kalendrio<br>News Blog</h3><hr>
  <p>Bleiben Sie immer auf dem Laufenden<br>&amp; erfahren Sie alle Neuigkeiten.</p>
  <div class="link"><b>›</b>Weiter zum Kalendrio-Blog</div>
</div>

<div class="abs footer-top"><div class="brand"><i></i>Kalendrio</div></div>
<footer class="abs footer">
  <div class="col" style="left:214px"><span>© 2018 Alle Rechte vorbehalten</span></div>
  <div class="lang">Sprachauswahl <b style="font-weight:500">DE ⌄</b></div>
  <div class="col" style="left:492px"><strong>Sonstiges</strong><span>Home</span><span>Kontakt</span><span>Newsletter</span><span>Webinare</span></div>
  <div class="col" style="left:574px"><strong>Benutzer</strong><span>Login</span><span>Konto erstellen</span></div>
  <div class="col" style="left:671px"><strong>Rechtliches</strong><span>Impressum</span><span>AGB</span><span>Datenschutz</span><span>Sitemap</span></div>
  <div class="col" style="left:799px;line-height:12px"><strong style="margin-bottom:10px">Bewertungen durch Wertwelle.de</strong><span style="font-size:8px">Verknüpfen Sie jetzt Kalendrio mit<br>Wertwelle.de und profitieren Sie von<br>vertrauensvollen Usern und Transparenz.</span></div>
  <div class="btn">zu Wertwelle.de wechseln</div>
</footer>

</body>
</html>
```